Plantwise Mechanics Partners. Needs a Business Card Design

We need a business card design for an engineering company which supplies industrial components (pumps, compressors, mechanical seals) provides repairs and services for above mentioned equipments. We offer a uniqe engineering solutions which help our customers to increase the productivness of their manufacturings, and energy savings.

Target Market(s)

Chemical and energy plants, refineries. Food industry and private consumers in a less.

Industry/Entity Type

Business

Contact Information for Business Card

Stylish and sleek design oriented on industrial area.

Requirements
Should not have
• company name shortening

```html
<!DOCTYPE html>
<html lang="en">
<head>
<meta charset="utf-8">
<title>Plantwise Mechanics Partners – Business Card</title>
<link rel="stylesheet" href="https://fonts.googleapis.com/css2?family=PT+Sans:wght@400;700&display=swap">
<style>
  :root {
    --canvas-bg: #e9e7e3;
    --card-white: #ffffff;
    --brand-blue: #1f3f8f;
    --card-blue: #2a54b0;
    --card-blue-deep: #1e3f94;
    --card-blue-light: #4c74c8;
    --accent-red: #e8435a;
    --accent-orange: #f3a33a;
    --text-light: #ffffff;
  }
  * { box-sizing: border-box; margin: 0; padding: 0; }
  html, body { width: 1200px; height: 843px; overflow: hidden; }
  body {
    background: var(--canvas-bg);
    font-family: "PT Sans", sans-serif;
    display: flex;
    align-items: center;
    justify-content: center;
    gap: 40px;
  }
  .card {
    width: 540px;
    height: 309px;
    position: relative;
    overflow: hidden;
    box-shadow: 0 6px 18px rgba(0,0,0,0.18);
  }
  /* Front side */
  .card-front {
    background: var(--card-white);
    display: flex;
    flex-direction: column;
    align-items: center;
    justify-content: center;
    gap: 14px;
  }
  .brand-mark {
    width: 62px; height: 62px;
    border-radius: 50%;
    background: var(--brand-blue);
  }
  .brand-name {
    color: var(--brand-blue);
    font-weight: 700;
    font-size: 30px;
    letter-spacing: 0.2px;
  }
  /* Back side */
  .card-back {
    background: var(--card-blue);
    color: var(--text-light);
  }
  .swirl-field {
    position: absolute; inset: 0;
    background: radial-gradient(circle at 50% 50%, var(--card-blue-light) 0%, var(--card-blue) 45%, var(--card-blue-deep) 100%);
  }
  .holder {
    position: absolute;
    left: 26px; top: 24px;
    line-height: 1.2;
  }
  .holder-name {
    color: var(--accent-red);
    font-size: 18px;
    letter-spacing: 0.5px;
    text-transform: uppercase;
  }
  .holder-title {
    color: var(--accent-orange);
    font-size: 15px;
  }
  .holder-address {
    font-size: 15px;
    margin-top: 2px;
  }
  .center-seal {
    position: absolute;
    left: 50%; top: 50%;
    width: 116px; height: 116px;
    transform: translate(-50%, -50%);
    border-radius: 50%;
    background: var(--card-white);
    display: flex;
    align-items: center;
    justify-content: center;
    text-align: center;
    color: var(--brand-blue);
    font-weight: 700;
    font-size: 13px;
    line-height: 1.15;
    padding: 12px;
  }
  .contacts {
    position: absolute;
    right: 22px; bottom: 20px;
    list-style: none;
    font-size: 15px;
    line-height: 1.45;
  }
  .contacts li {
    display: flex;
    align-items: center;
    justify-content: flex-end;
    gap: 8px;
  }
  .contacts svg { width: 13px; height: 13px; fill: var(--accent-red); }
</style>
</head>
<body>
  <section class="card card-front">
    <div class="brand-mark" aria-hidden="true"></div>
    <div class="brand-name">Plantwise Mechanics Partners</div>
  </section>

  <section class="card card-back">
    <div class="swirl-field" role="img" aria-label="Radiating swirl pattern in shades of blue"></div>
    <div class="holder">
      <div class="holder-name">Daniel Harper</div>
      <div class="holder-title">CEO/Founder</div>
      <div class="holder-address">1420 Foundry Road<br>Tacoma, Washington 98402</div>
    </div>
    <div class="center-seal">Plantwise Mechanics Partners</div>
    <ul class="contacts">
      <li>555 210 4478
        <svg viewBox="0 0 16 16" aria-hidden="true"><path d="M3 1l3 0 1 4-2 1c1 2 3 4 5 5l1-2 4 1 0 3c0 1-1 2-2 2C7 15 1 9 1 3c0-1 1-2 2-2z"/></svg>
      </li>
      <li>555 318 9026
        <svg viewBox="0 0 16 16" aria-hidden="true"><path d="M4 0h8v16H4z M5.5 2v10h5V2z"/></svg>
      </li>
      <li>info@plantwisemech.com
        <svg viewBox="0 0 16 16" aria-hidden="true"><path d="M0 3h16v10H0z M1.5 4.5L8 9l6.5-4.5z" fill-rule="evenodd"/></svg>
      </li>
      <li>www.plantwisemech.com
        <svg viewBox="0 0 16 16" aria-hidden="true"><circle cx="8" cy="8" r="7.5"/></svg>
      </li>
    </ul>
  </section>
</body>
</html>
```